Mosquito and outdoor pest management

The uploaded logo must be integrated as the main theme of the card. I would like it to be modern and eye catching. Maybe some backround images or light silver metallic background.
Space enough at the base for contact info to be put in- phone numbers,emails,names,website.
Space on the back for short blog and lines for hand writing..calling card.
Target Market(s)
Commercial- golf courses, schools, outdoor function properties, pre event treatments.
Residential- retirement villages, townhome complexes and general houses
Industry/Entity Type
Management

```html
<!DOCTYPE html>
<html lang="en">
<head>
<meta charset="utf-8">
<title>Braymoor Mosquito – Business Card</title>
<link rel="stylesheet" href="https://fonts.googleapis.com/css2?family=Montserrat:wght@400;500;700&display=swap">
<style>
  :root {
    --canvas-bg: #e4e4e4;
    --card-white: #ffffff;
    --card-black: #050505;
    --brand-red: #e0141e;
    --ink-dark: #1b1b1b;
    --ink-light: #ffffff;
    --card-w: 600px;
    --card-h: 343px;
  }
  * { box-sizing: border-box; margin: 0; padding: 0; }
  html, body {
    width: 1200px;
    height: 800px;
    overflow: hidden;
    background: var(--canvas-bg);
    font-family: "Montserrat", Arial, sans-serif;
  }
  .sheet {
    width: 1200px;
    height: 800px;
    display: flex;
    flex-direction: column;
    align-items: center;
    justify-content: center;
    gap: 30px;
  }
  .card {
    position: relative;
    width: var(--card-w);
    height: var(--card-h);
    border-radius: 14px;
    overflow: hidden;
    box-shadow: 0 6px 18px rgba(0, 0, 0, 0.25);
  }

  /* Front */
  .card--front { background: var(--card-white); }
  .card__swoosh {
    position: absolute;
    inset: 0;
    width: 100%;
    height: 100%;
  }
  .brand {
    position: absolute;
    left: 0;
    right: 0;
    top: 86px;
    display: flex;
    align-items: center;
    justify-content: center;
    gap: 12px;
  }
  .brand__dot {
    width: 18px;
    height: 18px;
    border-radius: 50%;
    background: var(--brand-red);
  }
  .brand__name {
    font-weight: 700;
    font-size: 34px;
    letter-spacing: 1px;
    text-transform: uppercase;
    color: var(--ink-dark);
  }
  .contact {
    position: absolute;
    left: 30px;
    bottom: 26px;
    list-style: none;
    display: flex;
    flex-direction: column;
    gap: 4px;
  }
  .contact__item {
    display: flex;
    align-items: center;
    gap: 10px;
    color: var(--ink-light);
    font-size: 14px;
    line-height: 17px;
  }
  .contact__icon {
    width: 15px;
    height: 15px;
    flex: none;
  }
  .person {
    position: absolute;
    right: 30px;
    top: 232px;
    text-align: right;
  }
  .person__name {
    color: var(--brand-red);
    font-weight: 700;
    font-size: 17px;
    letter-spacing: 0.5px;
    text-transform: uppercase;
  }
  .person__role {
    color: var(--ink-light);
    font-size: 13px;
    margin-top: 4px;
  }

  /* Back */
  .card--back {
    background: var(--card-black);
    display: flex;
    align-items: center;
    justify-content: center;
  }
  .card--back .brand {
    position: static;
  }
  .card--back .brand__name { color: var(--ink-light); }
</style>
</head>
<body>
<main class="sheet">

  <section class="card card--front" aria-label="Business card front">
    <svg class="card__swoosh" viewBox="0 0 600 343" preserveAspectRatio="none" aria-hidden="true">
      <path d="M0,214 Q300,186 600,172 L600,194 Q300,200 0,217 Z" fill="var(--brand-red)"/>
      <path d="M0,220 Q300,204 600,198 L600,343 L0,343 Z" fill="var(--card-black)"/>
    </svg>

    <div class="brand">
      <span class="brand__dot"></span>
      <span class="brand__name">Braymoor Mosquito</span>
    </div>

    <ul class="contact">
      <li class="contact__item">
        <svg class="contact__icon" viewBox="0 0 16 16" aria-hidden="true">
          <rect width="16" height="16" rx="3" fill="var(--brand-red)"/>
          <path d="M5 3.5 L6.8 5.6 L5.9 6.8 Q7 9 9.2 10.1 L10.4 9.2 L12.5 11 L11.4 12.5 Q7.5 12.3 3.5 4.6 Z" fill="#000"/>
        </svg>
        555.014.2270
      </li>
      <li class="contact__item">
        <svg class="contact__icon" viewBox="0 0 16 16" aria-hidden="true">
          <rect width="16" height="16" rx="3" fill="var(--brand-red)"/>
          <rect x="5" y="3" width="6" height="3" fill="#000"/>
          <rect x="3" y="6.5" width="10" height="4.5" rx="1" fill="#000"/>
          <rect x="5" y="10" width="6" height="3" fill="#000"/>
        </svg>
        555.014.2271
      </li>
      <li class="contact__item">
        <svg class="contact__icon" viewBox="0 0 16 16" aria-hidden="true">
          <rect width="16" height="16" rx="3" fill="var(--brand-red)"/>
          <rect x="3" y="4.5" width="10" height="7" fill="none" stroke="#000" stroke-width="1.3"/>
          <path d="M3 4.5 L8 8.7 L13 4.5" fill="none" stroke="#000" stroke-width="1.3"/>
        </svg>
        info@braymoorpest.com
      </li>
      <li class="contact__item">
        <svg class="contact__icon" viewBox="0 0 16 16" aria-hidden="true">
          <rect width="16" height="16" rx="3" fill="var(--brand-red)"/>
          <circle cx="8" cy="8" r="4.8" fill="none" stroke="#000" stroke-width="1.2"/>
          <ellipse cx="8" cy="8" rx="2" ry="4.8" fill="none" stroke="#000" stroke-width="1"/>
          <path d="M3.2 8 H12.8" stroke="#000" stroke-width="1"/>
        </svg>
        www.braymoorpest.com
      </li>
    </ul>

    <div class="person">
      <p class="person__name">Jordan Hale</p>
      <p class="person__role">General Manager</p>
    </div>
  </section>

  <section class="card card--back" aria-label="Business card back">
    <div class="brand">
      <span class="brand__dot"></span>
      <span class="brand__name">Braymoor Mosquito</span>
    </div>
  </section>

</main>
</body>
</html>
```